KTR Business Card

We need a new design for our business cards. We are brokers in the scrap metal industry and wants something nice, clean and very professional.

Industry/Entity Type

Business

Requirements
Must have
• Our logo
• Would probably be good to incorporate colors from logo into design.
• Example info we need on the cards.
• Name
• Company Address
• Cell Phone
• Office Phone
• Fax
• Email
• Company Website
Should not have
• Should not be too cluttered. Needs to be nice, clean and professional looking.

```html
<!DOCTYPE html>
<html lang="en">
<head>
<meta charset="utf-8">
<title>KTR Business Card</title>
<link rel="stylesheet" href="https://fonts.googleapis.com/css2?family=Barlow:wght@400;500;600&display=swap">
<style>
  :root {
    --page-bg: #e9e9eb;
    --card-white: #f3f3f4;
    --navy-deep: #0b3a5e;
    --navy-bright: #0a6499;
    --brand-blue: #1a6aa6;
    --brand-red: #c42128;
    --ink: #2b2b2e;
    --ink-soft: #55575c;
    --rule: #2f6fa3;
    --web-blue: #1c5f98;
  }
  * { margin: 0; padding: 0; box-sizing: border-box; }
  html, body { width: 1200px; height: 900px; overflow: hidden; }
  body {
    background: var(--page-bg);
    font-family: "Barlow", Arial, sans-serif;
    display: flex;
    flex-direction: column;
    align-items: center;
    justify-content: center;
    gap: 44px;
  }
  .card {
    width: 640px;
    height: 366px;
    position: relative;
    box-shadow: 0 6px 18px rgba(0,0,0,.14);
  }

  /* Front */
  .card-front { background: var(--card-white); display: flex; }
  .brand-block {
    width: 50%;
    display: flex;
    flex-direction: column;
    align-items: center;
    justify-content: center;
    gap: 14px;
  }
  .brand-mark { display: flex; align-items: center; gap: 12px; }
  .brand-square { width: 44px; height: 44px; background: var(--brand-blue); }
  .brand-initials {
    font-size: 52px; font-weight: 600; color: var(--brand-blue);
    letter-spacing: 2px; line-height: 1;
  }
  .brand-name { font-size: 21px; font-weight: 600; color: var(--ink); }
  .divider {
    position: absolute; left: 50%; top: 54px; bottom: 54px;
    width: 1px; background: var(--rule);
  }
  .details {
    width: 50%;
    padding: 64px 0 0 32px;
    color: var(--ink-soft);
  }
  .person-name {
    font-size: 21px; font-weight: 500; color: var(--ink);
    letter-spacing: .5px; text-transform: uppercase;
  }
  .person-title { font-size: 13px; margin-bottom: 18px; }
  .contact-list { list-style: none; font-size: 13px; line-height: 1.5; }
  .contact-list .label {
    display: inline-block; width: 16px; color: var(--brand-red); font-weight: 500;
  }
  .address { font-size: 13px; line-height: 1.5; margin-top: 18px; }
  .website { font-size: 13px; color: var(--web-blue); margin-top: 10px; }

  /* Back */
  .card-back {
    background: linear-gradient(135deg, var(--navy-deep) 0%, var(--navy-bright) 100%);
    display: flex; align-items: center; justify-content: center;
  }
  .back-mark { display: flex; align-items: center; gap: 14px; }
  .back-mark .brand-square { background: #ffffff; width: 50px; height: 50px; }
  .back-mark .brand-initials { color: #ffffff; font-size: 60px; }
  .back-website {
    position: absolute; right: 36px; bottom: 34px;
    font-size: 13px; color: #cfe0ee; letter-spacing: .6px;
  }
</style>
</head>
<body>
  <section class="card card-front">
    <div class="brand-block">
      <div class="brand-mark">
        <span class="brand-square"></span>
        <span class="brand-initials">KTR</span>
      </div>
      <div class="brand-name">Keystone Trade Resources</div>
    </div>
    <span class="divider"></span>
    <div class="details">
      <h1 class="person-name">Dana Whitfield</h1>
      <p class="person-title">Director</p>
      <ul class="contact-list">
        <li><span class="label">T</span>(555) 210-4388</li>
        <li><span class="label">F</span>(555) 210-4377</li>
        <li><span class="label">E</span>info@keystonetraderesources.com</li>
      </ul>
      <p class="address">2240 Harbor Ave.<br>Riverton, SC 29040</p>
      <p class="website">www.keystonetraderesources.com</p>
    </div>
  </section>

  <section class="card card-back">
    <div class="back-mark">
      <span class="brand-square"></span>
      <span class="brand-initials">KTR</span>
    </div>
    <p class="back-website">www.keystonetraderesources.com</p>
  </section>
</body>
</html>
```